Brain Science Music company needs modern clean website

We're looking for a website that's very clean and modern but also has some nice bold (futuristic) colors in it. The design should communicate a company that's providing something new and fresh! We'd greatly appreciate web designs similar to: https://thebrightfolio.co/

Lumen Cascade is a US-based Neuroscience music company that offers state-of-the-art technology solutions that help people focus, relax and sleep with the help of scientifically engineered music.

Target Market(s)

US businesses looking for specialized neuroscience music technology.

Logo Text

LumenCascade or LC

Coding

Coded - Design and coding required

Number of Pages Required

1 page

Font styles to use
Sans Serif

Colors

Designer to choose colors to be used in the design.

Requirements
Nice to have
• A website similar to: https://thebrightfolio.co/
We like the colors, the fonts, the simple design layouts and the colorful images.

```html
<!DOCTYPE html>
<html lang="en">
<head>
<meta charset="utf-8">
<title>LumenCascade — Science-driven music</title>
<link href="https://fonts.googleapis.com/css2?family=Noto+Sans:wght@400;500;600;700&family=Roboto:wght@400;500&display=swap" rel="stylesheet">
<style>
  :root{
    --ink:#16112a;
    --text:#2f2b3a;
    --pink:#fb3468;
    --sun:#fcc866;
    --sky:#45d3f0;
    --band:#f2f6fd;
    --night:#22063f;
    --white:#ffffff;
  }
  *{box-sizing:border-box;margin:0;padding:0}
  html,body{width:1200px;height:2895px;overflow:hidden;background:var(--white)}
  body{position:relative;font-family:'Noto Sans',sans-serif;color:var(--text)}
  .abs{position:absolute}

  .brand{left:107px;top:62px;font-size:15px;font-weight:700;color:var(--ink)}
  .nav{top:64px;font-family:'Roboto',sans-serif;font-size:14px;color:var(--ink)}

  .hero-title{left:109px;top:178px;font-size:42px;line-height:45px;font-weight:600;color:var(--ink)}
  .hero-sub{left:109px;top:278px;font-size:17px;line-height:27px}
  .btn{left:109px;top:364px;width:233px;height:40px;border-radius:20px;background:var(--pink);color:var(--white);
       font-size:13px;letter-spacing:.8px;font-weight:500;display:flex;align-items:center;justify-content:center;gap:12px}
  .btn svg{width:11px;height:11px}
  .hero-art{left:593px;top:101px;width:463px;height:365px;border-radius:46% 54% 40% 60%/50% 45% 55% 50%;
       background:radial-gradient(circle at 40% 45%,var(--sky) 0 30%,transparent 55%),
                  radial-gradient(circle at 70% 30%,var(--pink) 0 18%,transparent 40%),
                  radial-gradient(circle at 60% 80%,var(--night) 0 16%,transparent 38%),
                  linear-gradient(135deg,#dde5f7,#f5f0ff)}

  .eyebrow{font-size:13px;letter-spacing:.6px;font-weight:500;color:var(--ink)}
  .music-for{left:109px;top:548px}
  .card{top:601px;width:200px;text-align:center}
  .card-art{height:126px;border-radius:10px;background:linear-gradient(160deg,#e8edfa 0%,var(--sun) 55%,var(--pink) 100%);opacity:.85}
  .card:nth-child(odd) .card-art{background:linear-gradient(160deg,#e8edfa 0%,var(--sky) 55%,var(--pink) 100%)}
  .card-label{margin-top:22px;font-size:30px;color:var(--ink)}

  .band{left:0;top:908px;width:1200px;height:632px;background:var(--band)}
  .band-title{left:109px;top:983px;font-size:42px;line-height:44px;font-weight:600;color:var(--ink)}
  .fact{left:526px;width:480px;display:flex;gap:17px}
  .fact-icon{flex:none;width:65px;height:65px;border-radius:50%;background:var(--sun);display:flex;align-items:center;justify-content:center}
  .fact-icon svg{width:40px;height:40px;stroke:var(--pink);fill:none;stroke-width:1.6;stroke-linecap:round}
  .fact p{font-size:17.5px;line-height:27px;padding-top:4px;width:398px}

  .story-title{left:108px;top:1708px;font-size:42px;font-weight:600;color:var(--ink)}
  .story{left:108px;top:1796px;width:490px;font-size:17.5px;line-height:27px}
  .story p+p{margin-top:26px}
  .photo-back{left:668px;top:1790px;width:350px;height:392px;border-radius:18px;background:var(--sun);transform:rotate(-5deg)}
  .photo{left:673px;top:1776px;width:338px;height:408px;border-radius:18px;transform:rotate(-3deg);
         background:linear-gradient(170deg,#6d7a52 0%,#a39b7c 40%,#cfd9e6 75%,#e9eef6 100%)}

  .footer{left:0;top:2609px;width:1200px;height:286px;background:var(--night);color:var(--white)}
  .footer-brand{left:108px;top:2650px;font-size:30px;font-weight:500;color:var(--white)}
  .footer-eyebrow{left:608px;top:2666px;color:var(--white)}
  .footer-links{left:608px;top:2703px;list-style:none;font-size:17.5px;line-height:37px;color:var(--white)}
  .social{top:2799px;width:34px;height:34px;border-radius:50%;background:var(--white);display:flex;align-items:center;justify-content:center}
  .social span{width:10px;height:10px;border-radius:50%;background:var(--pink)}
</style>
</head>
<body>
  <header>
    <div class="abs brand">LumenCascade</div>
    <nav>
      <span class="abs nav" style="left:858px">Music</span>
      <span class="abs nav" style="left:938px">About us</span>
      <span class="abs nav" style="left:1035px">Contacts</span>
    </nav>
  </header>

  <section class="hero">
    <h1 class="abs hero-title">The new frontier<br>of music and the brain</h1>
    <p class="abs hero-sub">Science-driven music<br>for relaxation and productivity</p>
    <div class="abs btn">TRY NOW <svg viewBox="0 0 10 10"><path d="M1 0 L10 5 L1 10Z" fill="#fff"/></svg></div>
    <div class="abs hero-art" role="img" aria-label="Illustration of a woman listening to music on headphones among clouds and notes"></div>
  </section>

  <section class="categories">
    <div class="abs eyebrow music-for">MUSIC FOR</div>
    <div>
      <div class="abs card" style="left:125px"><div class="card-art" role="img" aria-label="Illustration of a person working on a laptop"></div><div class="card-label">Productivity</div></div>
      <div class="abs card" style="left:374px"><div class="card-art" role="img" aria-label="Illustration of a person sleeping"></div><div class="card-label">Sleep</div></div>
      <div class="abs card" style="left:625px"><div class="card-art" role="img" aria-label="Illustration of a person meditating"></div><div class="card-label">Meditation</div></div>
      <div class="abs card" style="left:874px"><div class="card-art" role="img" aria-label="Illustration of a person exercising"></div><div class="card-label">Athletics</div></div>
    </div>
  </section>

  <section class="entrainment">
    <div class="abs band"></div>
    <h2 class="abs band-title">Brainwave<br>Entrainment</h2>
    <div class="abs fact" style="top:990px">
      <div class="fact-icon"><svg viewBox="0 0 40 40"><path d="M20 8c-4-3-11-1-11 5-4 2-4 9 0 11 0 6 7 8 11 5 4 3 11 1 11-5 4-2 4-9 0-11 0-6-7-8-11-5zM20 8v21M14 14c2 1 3 3 2 5M26 14c-2 1-3 3-2 5M13 23c2 0 4 1 4 3M27 23c-2 0-4 1-4 3"/></svg></div>
      <p>Neurons in our brains communicate with each other, forming thoughts, emotions, and ideas using electrical impulses (commonly known as Brainwaves).</p>
    </div>
    <div class="abs fact" style="top:1131px">
      <div class="fact-icon"><svg viewBox="0 0 40 40"><path d="M4 14c4-4 8 4 12 0s8 4 12 0 6 2 8 0M4 20c4-4 8 4 12 0s8 4 12 0 6 2 8 0M4 26c4-4 8 4 12 0s8 4 12 0 6 2 8 0"/></svg></div>
      <p>Activities such as sleeping, working, or meditating, each have their own unique brainwave pattern.</p>
    </div>
    <div class="abs fact" style="top:1244px">
      <div class="fact-icon"><svg viewBox="0 0 40 40"><circle cx="10" cy="10" r="2"/><circle cx="17" cy="10" r="2"/><circle cx="24" cy="10" r="2"/><circle cx="10" cy="17" r="2"/><circle cx="10" cy="24" r="2"/><path d="M20 30V17a2 2 0 0 1 4 0v8l6 1c2 0 3 2 2 4l-2 5h-8z"/></svg></div>
      <p>Lumen Cascade leverages Musical Phase Locking, to optimize brainwave patterns for each desired activity.</p>
    </div>
    <div class="abs fact" style="top:1357px">
      <div class="fact-icon"><svg viewBox="0 0 40 40"><path d="M6 16h28v16H6zM20 16v16M10 21h6M10 26h6M24 21h6M24 26h6M17 10a3 3 0 1 1 6 0c0 2-2 2-2 4h-2c0-2-2-2-2-4z"/></svg></div>
      <p>Our music is driven by science. We utilize large scale studies and data from electro-encephlograms to produce substantial results.</p>
    </div>
  </section>

  <section class="founder">
    <h2 class="abs story-title">Elias’s Story</h2>
    <div class="abs story">
      <p>Founder and Team Leader of Lumen Cascade, in conjunction with primary scientific advisor Dr. Helena Marsh. Elias is a pioneer in the neuroscience of music, and key innovator on the technology of Musical Phase Locking.</p>
      <p>At the age of 10, Elias wrote his first symphony and began studying music composition.</p>
      <p>After exposure to alpha waves in music, Elias began a lifelong pursuit of merging neuroscience and music composition.</p>
      <p>Elias founded Clearfield Labs in 2003, creating audio workstations for those who wanted to experience the effects of music guided by neuroscience, as well as software for brain-computer interfaces.</p>
      <p>As the science progressed and Clearfield Labs grew, Elias decided to form Tonewave.fm in 2014, a website and app that allowed nearly anybody to access the music, not just those who were scientifically minded.</p>
      <p>Lumen Cascade was formed to further the vision of neuroscience-based music becoming a daily resource that everyone should experience.</p>
    </div>
    <div class="abs photo-back"></div>
    <div class="abs photo" role="img" aria-label="Portrait photograph of the founder outdoors"></div>
  </section>

  <footer>
    <div class="abs footer"></div>
    <div class="abs footer-brand">LumenCascade</div>
    <div class="abs eyebrow footer-eyebrow">MUSIC FOR</div>
    <ul class="abs footer-links">
      <li>Productivity</li><li>Sleep</li><li>Meditation</li><li>Athletics</li>
    </ul>
    <div class="abs social" style="left:108px" aria-label="Social One"><span></span></div>
    <div class="abs social" style="left:154px" aria-label="Social Two"><span></span></div>
    <div class="abs social" style="left:200px" aria-label="Social Three"><span></span></div>
  </footer>
</body>
</html>
```